Assisted living facility needs a business card design

We need a business card design for an assisted living facility in Los Angeles. We have a logo selected but we would like a business card design that will leave a lasting impression on families looking to place their elderly loved ones in our care as well as on other facility providers who may refer their elderly residents to our facility.

```html
<!DOCTYPE html>
<html lang="en">
<head>
<meta charset="utf-8">
<title>Harborview Crest Senior Living – Business Card</title>
<link href="https://fonts.googleapis.com/css2?family=Marcellus&family=Work+Sans:wght@400;500&display=swap" rel="stylesheet">
<style>
  :root {
    --backdrop: #bfc0c3;
    --card: #ffffff;
    --brand-blue: #1f6fba;
    --ink-grey: #6f6f72;
    --rule-grey: #8a8a8d;
    --map-light: #ececee;
    --map-mid: #dadadd;
  }
  * { margin: 0; padding: 0; box-sizing: border-box; }
  html, body {
    width: 1200px; height: 876px; overflow: hidden;
    background: radial-gradient(ellipse at 55% 35%, #d4d5d8 0%, var(--backdrop) 70%, #a9aaad 100%);
  }
  .canvas { position: relative; width: 1200px; height: 876px; }
  .card {
    position: absolute; width: 510px; height: 292px;
    background: var(--card);
    box-shadow: 0 10px 24px rgba(0,0,0,0.18);
  }
  .card--front { left: 60px; top: 292px; }
  .card--back { left: 630px; top: 292px; }

  .brand {
    position: absolute; display: flex; align-items: center; justify-content: center; gap: 8px;
    font-family: "Work Sans", sans-serif; font-weight: 500;
    color: var(--brand-blue); white-space: nowrap;
  }
  .brand__dot { width: 10px; height: 10px; border-radius: 50%; background: var(--brand-blue); flex: none; }
  .card--front .brand { left: 200px; top: 48px; width: 290px; font-size: 18px; }
  .card--back .brand { left: 40px; top: 128px; width: 430px; font-size: 26px; }
  .card--back .brand__dot { width: 14px; height: 14px; }

  .person { position: absolute; left: 235px; top: 130px; width: 240px; text-align: center; }
  .person__name {
    font-family: "Marcellus", serif; font-size: 22px;
    color: var(--brand-blue); letter-spacing: 1px; text-transform: uppercase;
  }
  .person__role {
    display: flex; align-items: center; justify-content: center; gap: 10px;
    margin-top: 6px; font-family: "Work Sans", sans-serif; font-size: 12px;
    color: var(--ink-grey); letter-spacing: 1px;
  }
  .person__role::before, .person__role::after {
    content: ""; width: 50px; height: 1px; background: var(--rule-grey);
  }

  .contact {
    position: absolute; left: 26px; top: 120px; list-style: none;
    font-family: "Work Sans", sans-serif; font-size: 12px; color: var(--ink-grey);
  }
  .contact li { display: flex; align-items: center; gap: 7px; margin-bottom: 9px; }
  .contact svg { width: 11px; height: 11px; fill: var(--brand-blue); flex: none; }

  .address {
    position: absolute; right: 30px; bottom: 30px; text-align: right;
    font-family: "Work Sans", sans-serif; font-size: 13px; line-height: 1.6;
    color: var(--ink-grey); font-style: normal;
  }

  .world-map {
    position: absolute; left: 60px; top: 26px; width: 400px; height: 240px;
    border-radius: 6px;
    background: linear-gradient(160deg, var(--map-mid) 0%, var(--map-light) 100%);
  }
</style>
</head>
<body>
<main class="canvas">
  <section class="card card--front" aria-label="Card front">
    <div class="brand"><span class="brand__dot"></span>Harborview Crest Senior Living</div>
    <div class="person">
      <p class="person__name">Daniel R Hale</p>
      <p class="person__role">President</p>
    </div>
    <ul class="contact">
      <li><svg viewBox="0 0 24 24"><path d="M6.6 10.8a15.1 15.1 0 0 0 6.6 6.6l2.2-2.2c.3-.3.7-.4 1-.2 1.1.4 2.3.6 3.6.6.6 0 1 .4 1 1V20c0 .6-.4 1-1 1A17 17 0 0 1 3 4c0-.6.4-1 1-1h3.5c.6 0 1 .4 1 1 0 1.3.2 2.5.6 3.6.1.3 0 .7-.2 1z"/></svg>555-014-2287</li>
      <li><svg viewBox="0 0 24 24"><path d="M2 5h20v14H2zm2 2v.5l8 5 8-5V7zm0 3v7h16v-7l-8 5z"/></svg>info@harborviewcrest.com</li>
      <li><svg viewBox="0 0 24 24"><circle cx="12" cy="12" r="10"/></svg>www.harborviewcrest.com</li>
    </ul>
    <address class="address">1850 Maple Grove Lane<br>Fairview, CA 90210</address>
  </section>

  <section class="card card--back" aria-label="Card back">
    <div class="world-map" role="img" aria-label="Dotted world map in light grey"></div>
    <div class="brand"><span class="brand__dot"></span>Harborview Crest Senior Living</div>
  </section>
</main>
</body>
</html>
```